plain square mark valdremo remodel

Redesign plain square mark page to match website style with more dynamic capabilities, messaging, commerce, etc.

My website address is:
Www.valdremo.consulting for corporate styling, and flavour of approach and service offered.

Target Market(s)

Small, Medium Enterprise looking for business coaching and single entrepreneurs startups looking for advice and coaching.

Font styles to use
Sans Serif

Colors
276eb1

Requirements
Must have
• Match plain square mark page style to website for branding.
• Contact information
• Services offered
• Links to website, email, Twitter, blogging. Messaging.
• (Will upload images and other data soonest).
Nice to have
• E-commerce,

```html
<!DOCTYPE html>
<html lang="en">
<head>
<meta charset="utf-8">
<title>Brightmere Advisory – Page Cover</title>
<link rel="stylesheet" href="https://fonts.googleapis.com/css2?family=Roboto+Condensed:wght@400&family=Montserrat:wght@400;700&family=Roboto:wght@400;500;700&display=swap">
<style>
  :root {
    --topbar: #3b5998;
    --topbar-line: #29487d;
    --page-bg: #e9ebee;
    --brand: #276eb1;
    --brand-deep: #0f4e8a;
    --ink: #1d2129;
    --muted: #90949c;
    --white: #ffffff;
    --btn-border: #ccd0d5;
    --btn-bg: #f6f7f9;
    --cta: #4a86f0;
    --photo-a: #e9eef3;
    --photo-b: #b9c9d9;
    --photo-c: #6f8fb3;
  }
  * { box-sizing: border-box; margin: 0; padding: 0; }
  html, body { width: 1200px; height: 468px; overflow: hidden; background: var(--page-bg); }
  body { position: relative; font-family: "Roboto", Arial, sans-serif; color: var(--ink); }

  /* top navigation bar */
  .topbar { position: absolute; left: 0; top: 0; width: 1200px; height: 48px; background: var(--topbar); border-bottom: 1px solid var(--topbar-line); }
  .site-mark { position: absolute; left: 48px; top: 12px; width: 26px; height: 26px; background: var(--white); border-radius: 3px; }
  .search { position: absolute; left: 82px; top: 11px; width: 508px; height: 28px; background: var(--white); border-radius: 3px; font-size: 15px; line-height: 28px; padding-left: 10px; }
  .search-icon { position: absolute; right: 12px; top: 6px; }
  .user { position: absolute; left: 838px; top: 11px; display: flex; align-items: center; gap: 8px; color: var(--white); font-size: 13px; font-weight: 700; }
  .avatar { width: 26px; height: 26px; background: var(--white); }
  .nav-home { position: absolute; left: 912px; top: 16px; color: var(--white); font-size: 13px; font-weight: 700; border-left: 1px solid var(--topbar-line); padding-left: 10px; }
  .nav-home .count { background: var(--topbar-line); border-radius: 2px; padding: 0 4px; margin-left: 4px; font-size: 11px; }
  .nav-icons { position: absolute; left: 1015px; top: 13px; display: flex; gap: 14px; }
  .nav-icons span { width: 22px; height: 22px; background: var(--topbar-line); border-radius: 50%; }
  .nav-icons span.square { border-radius: 3px; width: 30px; margin-left: 20px; }

  /* left column */
  .profile-photo { position: absolute; left: 46px; top: 63px; width: 196px; height: 194px; background: var(--white); border: 1px solid #d3d6db; border-radius: 3px; display: flex; align-items: center; justify-content: center; flex-direction: column; gap: 10px; }
  .profile-photo .dot { width: 22px; height: 22px; border-radius: 50%; background: var(--brand); }
  .profile-photo .word { font-family: "Roboto Condensed", Arial, sans-serif; font-size: 26px; color: var(--brand); }
  .page-name { position: absolute; left: 46px; top: 272px; font-size: 26px; line-height: 30px; color: var(--ink); }
  .verified { display: inline-block; width: 20px; height: 20px; border-radius: 50%; background: #7f7f7f; vertical-align: -2px; margin-left: 3px; position: relative; }
  .verified::after { content: ""; position: absolute; left: 7px; top: 3px; width: 5px; height: 10px; border: solid var(--white); border-width: 0 2px 2px 0; transform: rotate(45deg); }
  .handle { position: absolute; left: 46px; top: 336px; font-size: 14px; color: var(--muted); }
  .side-menu { position: absolute; left: 46px; top: 378px; width: 196px; list-style: none; }
  .side-menu li { height: 35px; line-height: 35px; padding-left: 12px; font-size: 15px; color: #4b4f56; }
  .side-menu li.active { background: #dddfe2; border-left: 3px solid var(--topbar); color: var(--ink); font-weight: 700; padding-left: 9px; }

  /* cover */
  .cover { position: absolute; left: 259px; top: 48px; width: 941px; height: 360px; background: var(--white); overflow: hidden; }
  .cover svg { position: absolute; left: 0; top: 0; }
  .cover-wordmark { position: absolute; right: 36px; top: 44px; display: flex; align-items: center; gap: 8px; font-family: "Roboto Condensed", Arial, sans-serif; font-size: 26px; color: var(--brand-deep); }
  .cover-wordmark .dot { width: 18px; height: 18px; border-radius: 50%; background: var(--brand-deep); }
  .services { position: absolute; right: 17px; top: 146px; list-style: none; text-align: right; font-family: "Roboto Condensed", Arial, sans-serif; font-size: 20px; color: var(--brand-deep); }
  .services li { height: 35px; line-height: 24px; }
  .address { position: absolute; right: 17px; top: 292px; font-family: "Roboto Condensed", Arial, sans-serif; font-size: 23px; color: var(--brand-deep); }
  .contact-line { position: absolute; right: 17px; top: 327px; font-family: "Roboto Condensed", Arial, sans-serif; font-size: 15px; color: var(--brand-deep); }
  .contact-line .sep { display: inline-block; width: 3px; height: 12px; background: var(--brand-deep); margin: 0 7px; vertical-align: -1px; }
  .headline { position: absolute; left: 11px; top: 272px; font-family: "Montserrat", Arial, sans-serif; font-size: 25px; line-height: 36px; color: var(--white); }
  .headline strong { font-weight: 700; }

  /* action row */
  .actions { position: absolute; left: 271px; top: 424px; display: flex; height: 31px; border: 1px solid var(--btn-border); border-radius: 2px; background: var(--btn-bg); }
  .actions span { padding: 0 14px; line-height: 29px; font-size: 14px; font-weight: 700; color: #4b4f56; border-right: 1px solid var(--btn-border); }
  .actions span:last-child { border-right: 0; }
  .contact-btn { position: absolute; left: 858px; top: 424px; width: 327px; height: 31px; background: var(--cta); border-radius: 2px; color: var(--white); font-size: 16px; font-weight: 700; text-align: center; line-height: 31px; }
</style>
</head>
<body>
  <header class="topbar">
    <div class="site-mark"></div>
    <div class="search">Brightmere Advisory
      <svg class="search-icon" width="16" height="16" viewBox="0 0 16 16"><circle cx="6.5" cy="6.5" r="5" fill="none" stroke="#4b4f56" stroke-width="2"/><line x1="10.5" y1="10.5" x2="15" y2="15" stroke="#4b4f56" stroke-width="2"/></svg>
    </div>
    <div class="user"><span class="avatar"></span>Sam</div>
    <div class="nav-home">Home<span class="count">5</span></div>
    <div class="nav-icons"><span></span><span></span><span></span><span class="square"></span></div>
  </header>

  <aside>
    <div class="profile-photo"><span class="dot"></span><span class="word">Brightmere</span></div>
    <h1 class="page-name">Brightmere<br>Advisory<span class="verified"></span></h1>
    <div class="handle">@BrightmereAdvisory</div>
    <ul class="side-menu">
      <li class="active">Home</li>
      <li>About</li>
      <li>Notes</li>
    </ul>
  </aside>

  <section class="cover">
    <svg width="941" height="360" viewBox="0 0 826 316" preserveAspectRatio="none">
      <defs>
        <linearGradient id="photoTone" x1="0" y1="0" x2="1" y2="1">
          <stop offset="0" stop-color="var(--photo-a)"/>
          <stop offset="0.55" stop-color="var(--photo-b)"/>
          <stop offset="1" stop-color="var(--photo-c)"/>
        </linearGradient>
        <clipPath id="photoArea"><path d="M0 0 H510 C585 70 560 230 395 316 H0 Z"/></clipPath>
      </defs>
      <g clip-path="url(#photoArea)">
        <rect role="img" aria-label="Photo of a smiling businessman in glasses working on a laptop in a bright office" width="826" height="316" fill="url(#photoTone)"/>
        <rect x="0" y="230" width="826" height="86" fill="var(--brand-deep)"/>
      </g>
      <path d="M510 0 C585 70 560 230 395 316" fill="none" stroke="var(--brand-deep)" stroke-width="4"/>
      <g stroke="var(--brand-deep)" stroke-width="3" fill="var(--brand-deep)">
        <line x1="548" y1="139" x2="588" y2="139"/><circle cx="590" cy="139" r="4"/>
        <line x1="540" y1="170" x2="605" y2="170"/><circle cx="607" cy="170" r="4"/>
        <line x1="525" y1="200" x2="553" y2="200"/><circle cx="555" cy="200" r="4"/>
        <line x1="505" y1="231" x2="546" y2="231"/><circle cx="548" cy="231" r="4"/>
      </g>
    </svg>
    <div class="cover-wordmark"><span class="dot"></span>Brightmere</div>
    <ul class="services">
      <li>Personal Business Coaching</li>
      <li>SME Business Consulting</li>
      <li>E-commerce Consulting services</li>
      <li>Ecommerce Marketing Coaching</li>
    </ul>
    <p class="address">22, Fenwick Road, Alnmouth, NE661QT</p>
    <p class="contact-line">Tel : +44-7700-900482<span class="sep"></span>marcus.hale@valdremo.consulting</p>
    <p class="headline">Are you looking for support in<br><strong>startups for advice and coaching</strong></p>
  </section>

  <div class="actions"><span>Liked ▾</span><span>Message</span><span>··· More ▾</span></div>
  <div class="contact-btn">Contact Us</div>
</body>
</html>
```